Villa Sereno needs a new website for its boutique apartment

We are a boutique apartment in Florence that rents out to tourists. We are looking to redesign our website. See the existing site at www.villaserenostay.example

Ideally redesigned site would enable us to easily add and change photos in the gallery and across the site.

The new logo for the apartment is currently under design but being based around the current house logo with a person standing inside.
Updates

Project Deadline Extended
Reason: The website design by the 1st Place designer has been long and drawn out and not led to the design that we were looking for. As such, we are extending the deadline for another 5 days to hopefully get new designs and options.

Target Market(s)

Global tourists

Industry/Entity Type

Accommodation

Coding

Coded - Design and coding required

Number of Pages Required

5+ page

Font styles to use
Sans Serif

Requirements
Must have
• Welcome page, gallery page, information page about apartment and availability page with link to booking sites. And option for another page with tourist information. We must be able to change the photos in the gallery with relative ease when required.
• The Villa Sereno font has been uploaded which is used with the logo and the new logo has been uploaded.
Nice to have
• Looking like a fun but professional hotel site
• Page info is located on www.villaserenostay.example site

```html
<!DOCTYPE html>
<html lang="en">
<head>
<meta charset="utf-8">
<title>Villa Sereno – Contact Us</title>
<link href="https://fonts.googleapis.com/css2?family=Open+Sans:wght@400;600&display=swap" rel="stylesheet">
<style>
:root{
  --accent:#f26f21;
  --ink:#222222;
  --text:#555555;
  --muted:#9a9a9a;
  --rule:#e4e4e4;
  --field:#cfcfcf;
  --partner:#d6d6d6;
  --bg:#ffffff;
}
*{box-sizing:border-box;margin:0;padding:0}
html,body{width:855px;height:1200px;overflow:hidden;background:var(--bg)}
body{font-family:"Open Sans",Arial,sans-serif;color:var(--text);position:relative}
.brand{position:absolute;display:flex;align-items:center;gap:6px;color:var(--ink);font-weight:400;letter-spacing:.5px}
.brand-mark{width:10px;height:10px;background:var(--ink)}
.site-header .brand{left:102px;top:26px;font-size:16px}
.main-nav{position:absolute;right:101px;top:28px;display:flex;gap:25px}
.main-nav a{font-size:10px;font-weight:600;color:var(--ink);text-decoration:none}
.main-nav a.current{color:var(--accent)}
.hero{position:absolute;left:0;top:72px;width:855px;height:270px;
  background:linear-gradient(100deg,#8a3a30 0%,#c9b9a8 30%,#d9e6e4 50%,#cfc3b5 75%,#a89a8c 100%)}
.hero-title{position:absolute;left:0;width:100%;top:124px;text-align:center;color:#fff;font-size:22px;font-weight:400}
.btn{display:block;background:var(--accent);color:#fff;font-weight:600;font-size:11px;text-align:center;text-decoration:none;border:0}
.hero .btn{position:absolute;left:347px;top:168px;width:161px;height:33px;line-height:33px}
.section-title{position:absolute;left:0;width:100%;text-align:center;font-size:15px;font-weight:400;color:#333}
.lead{position:absolute;left:0;width:100%;text-align:center;font-size:11.5px}
.lead a{color:var(--accent);text-decoration:none}
.rule{position:absolute;left:102px;width:651px;height:1px;background:var(--rule)}
.partners{position:absolute;left:110px;top:556px;width:635px;display:flex;justify-content:space-between}
.partner-badge{width:136px;height:30px;background:var(--partner);border-radius:4px}
.field{position:absolute;border:1px solid var(--field);font-size:8px;color:var(--muted);padding:13px 8px 0;text-transform:uppercase}
.send{position:absolute;left:373px;top:931px;width:109px;height:33px;line-height:33px}
.site-footer{position:absolute;left:0;top:1023px;width:855px;height:177px;border-top:1px solid var(--rule)}
.site-footer .brand{left:0;width:100%;justify-content:center;top:40px;font-size:16px}
.footer-nav{position:absolute;top:107px;left:0;width:100%;display:flex;justify-content:center;gap:25px}
.footer-nav a{font-size:10px;font-weight:600;color:#444;text-decoration:none}
.copyright{position:absolute;top:133px;width:100%;text-align:center;font-size:10px;font-weight:600;color:#444}
</style>
</head>
<body>
<header class="site-header">
  <div class="brand"><span class="brand-mark"></span>VILLA SERENO</div>
  <nav class="main-nav">
    <a href="#">HOME</a><a href="#">ABOUT US</a><a href="#">GALLERY</a><a href="#">INFO</a><a href="#">AVAILABILITY</a><a href="#" class="current">CONTACT US</a>
  </nav>
</header>

<section class="hero" role="img" aria-label="Apartment kitchen with red fridge, white chairs and tulips in a vase">
  <h1 class="hero-title">CONTACT US</h1>
  <a href="#" class="btn">MAKE RESERVATION</a>
</section>

<h2 class="section-title" style="top:398px">MAKE RESERVATIONS</h2>
<p class="lead" style="top:437px">You can contact us at: <a href="#">reservations@villaserenostay.example</a></p>
<div class="rule" style="top:483px"></div>

<h2 class="section-title" style="top:513px">RESERVATIONS ARE ALSO OPEN VIA</h2>
<div class="partners">
  <span class="partner-badge"></span><span class="partner-badge"></span><span class="partner-badge"></span><span class="partner-badge"></span>
</div>
<div class="rule" style="top:637px"></div>

<h2 class="section-title" style="top:682px">ENQUIRY</h2>
<p class="lead" style="top:712px">To make a booking enquiry, please use the contact form below:</p>

<form class="enquiry-form">
  <div class="field" style="left:158px;top:768px;width:262px;height:35px">Name</div>
  <div class="field" style="left:158px;top:821px;width:262px;height:35px">E-mail</div>
  <div class="field" style="left:158px;top:874px;width:262px;height:35px">Phone</div>
  <div class="field" style="left:436px;top:768px;width:262px;height:141px">Message</div>
  <span class="btn send">SEND</span>
</form>

<footer class="site-footer">
  <div class="brand"><span class="brand-mark"></span>VILLA SERENO</div>
  <nav class="footer-nav">
    <a href="#">HOME</a><a href="#">ABOUT US</a><a href="#">GALLERY</a><a href="#">INFO</a><a href="#">AVAILABILITY</a><a href="#">CONTACT US</a>
  </nav>
  <p class="copyright">© 2016 COMPANY NAME &nbsp;|&nbsp; ALL RIGHTS RESERVED</p>
</footer>
</body>
</html>
```